Med Spa business card design with logo

Need a logo design and business card for our new company Velora Skinworks Med Spa. We are a medical office that deals with high end clients. We offer them skin care products which include NERVAX, lip augmentation, and various laser for the skin. I king of like the logo attached, maybe something along those lines but also open to any logo concept.
Updates

Target Market(s)

Out target audience are male and females in the age range of 21-80 years of age

Industry/Entity Type

Medical

Contact Information for Business Card

woukd like front of card to have logo and business name VELORA SKINWORKS MEDSPA. Back of card employee name and phone number along with instagram logo and user name

Font styles to use
Serif
Sans Serif

Requirements
Must have
• prefer monochromatic look white, black, gold
Should not have
• not too colorful

```html
<!DOCTYPE html>
<html lang="en">
<head>
<meta charset="utf-8">
<title>Velora Skinworks Med Spa – Business Card</title>
<link href="https://fonts.googleapis.com/css2?family=Open+Sans:wght@400;600;700;800&display=swap" rel="stylesheet">
<style>
  :root{
    --stage:#1e1e20;
    --card-dark:#5b5b5e;
    --card-light:#ffffff;
    --ink:#3a3a3c;
    --ink-soft:#6d6d70;
    --white:#ffffff;
    --tab:#4a4a4c;
  }
  *{margin:0;padding:0;box-sizing:border-box}
  html,body{width:1200px;height:1000px;overflow:hidden}
  body{
    background:var(--stage);
    font-family:"Open Sans",Arial,sans-serif;
    display:flex;flex-direction:column;align-items:center;justify-content:center;gap:60px;
  }
  .card{
    width:640px;height:366px;border-radius:26px;position:relative;overflow:hidden;
  }
  .card--front{background:var(--card-dark);display:flex;align-items:center;justify-content:center}
  .front__mark{
    position:absolute;width:250px;height:250px;border-radius:50%;
    border:3px solid rgba(255,255,255,.08);left:50%;top:50%;transform:translate(-50%,-50%);
  }
  .front__title{
    position:relative;color:var(--white);font-weight:800;font-size:30px;letter-spacing:.5px;
  }
  .card--back{background:var(--card-light)}
  .back__tab{position:absolute;left:0;top:168px;width:12px;height:34px;background:var(--tab)}
  .back__title{
    position:absolute;left:52px;top:70px;color:var(--ink);font-weight:800;font-size:27px;letter-spacing:.4px;
  }
  .back__brand{
    position:absolute;right:44px;top:48px;display:flex;align-items:center;gap:8px;
    color:var(--ink);font-weight:800;font-size:15px;
  }
  .back__brand-dot{width:22px;height:22px;border-radius:50%;background:var(--ink-soft)}
  .person{position:absolute;left:58px;top:160px}
  .person__name{color:var(--ink);font-weight:800;font-size:20px;line-height:1.1}
  .person__role{color:var(--ink-soft);font-size:12px;font-weight:600}
  .address{position:absolute;left:72px;top:222px;color:var(--ink-soft);font-size:12.5px;line-height:1.35}
  .contacts{position:absolute;left:58px;top:270px;list-style:none;color:var(--ink);font-size:13px}
  .contacts li{display:flex;align-items:center;gap:10px;height:20px}
  .contacts svg{width:11px;height:11px;fill:var(--ink)}
</style>
</head>
<body>
  <section class="card card--front">
    <div class="front__mark"></div>
    <h1 class="front__title">VELORA SKINWORKS MEDSPA</h1>
  </section>

  <section class="card card--back">
    <div class="back__tab"></div>
    <h2 class="back__title">VELORA SKINWORKS MEDSPA</h2>
    <div class="back__brand"><span class="back__brand-dot"></span>VELORA</div>
    <div class="person">
      <p class="person__name">ADRIAN COLE</p>
      <p class="person__role">CEO &amp; FOUNDER</p>
    </div>
    <p class="address">Your Street Address,<br>NewYork, 1234</p>
    <ul class="contacts">
      <li><svg viewBox="0 0 24 24"><path d="M6.6 10.8a15 15 0 0 0 6.6 6.6l2.2-2.2a1 1 0 0 1 1-.25 11.4 11.4 0 0 0 3.6.57 1 1 0 0 1 1 1V20a1 1 0 0 1-1 1A17 17 0 0 1 3 4a1 1 0 0 1 1-1h3.5a1 1 0 0 1 1 1c0 1.25.2 2.45.57 3.57a1 1 0 0 1-.25 1z"/></svg>+000 123 456 789</li>
      <li><svg viewBox="0 0 24 24"><path d="M2 5h20v14H2z M2 5l10 8 10-8" fill="none" stroke="#3a3a3c" stroke-width="2.5"/></svg>yourname@email.com</li>
      <li><svg viewBox="0 0 24 24"><circle cx="12" cy="12" r="10"/></svg>www.websitename.com</li>
    </ul>
  </section>
</body>
</html>
```